Build a Web page - Dovin Pratchell Homes, LLC - a custom home builder

We are a custom home builder in Wisconsin. Need a basic web page with a home page, About Us, Contact info, Gallery, and Testimonials page. Gallery will probably have sub-pages and each will have about ten pictures or less. I already own the domain and have web hosting through Wix, I just need the site built. Once the page is built I should be able to do the upkeep on it myself. If I need to add pictures or whatever.
Updates

Project Deadline Extended
Reason: I am still looking through designs and will select soon - thank you!

Target Market(s)

Gen X and Millennials who are looking to build a home. Custom built homes - not generic spec homes.

Industry/Entity Type

Home Builder

Number of Pages Required

5+ page

Font styles to use
Sans Serif

Colors
ffffff
ec1f27
000000
9d9d9d

Requirements
Must have
• I have no idea if I want coded or in coded. I'm not sure of the difference and why I would want one over the other.
Nice to have
• We like the following colors - red, black, gray, white.
Should not have
• not a big fan of clip art like hammers, tape measures, etc. Must look professional.

```html
<!DOCTYPE html>
<html lang="en">
<head>
<meta charset="utf-8">
<title>Dovin Pratchell Homes, LLC</title>
<link href="https://fonts.googleapis.com/css2?family=Open+Sans:ital,wght@0,400;0,600;0,700;1,400&display=swap" rel="stylesheet">
<style>
:root{
  --red:#b3060d;
  --red-bright:#ec1f27;
  --black:#000;
  --dark:#1f1f1f;
  --footer:#262626;
  --grey:#9d9d9d;
  --light:#f3f3f3;
  --white:#fff;
  --text:#444;
  --maroon-a:#4a0f1c;
  --maroon-b:#8c1838;
}
*{box-sizing:border-box;margin:0;padding:0}
html,body{width:1200px;height:3186px;overflow:hidden}
body{font-family:"Open Sans",Arial,sans-serif;color:var(--text);background:var(--white);position:relative}
.abs{position:absolute}
.section{position:absolute;left:0;width:1200px}

/* header */
.header{top:0;height:127px;background:var(--black)}
.logo-area{left:0;top:0;width:310px;height:127px}
.brand{left:100px;top:10px;width:160px;height:108px;border:1px solid #ccc;display:flex;align-items:center;gap:8px;padding:0 10px}
.brand-mark{width:14px;height:14px;background:var(--red);flex:none}
.brand-name{color:var(--red);font-weight:700;font-size:15px;line-height:1.2;text-transform:uppercase}
.social{display:flex;gap:8px}
.social span{width:30px;height:30px;border:1px solid #555;display:block}
.header .social{left:314px;top:14px}
.contact-item{top:10px;display:flex;gap:10px;align-items:flex-start;color:var(--white);font-size:13px;line-height:1.35}
.contact-item small{font-size:11px;color:#ccc;display:block}
.contact-item .ic{width:32px;height:32px;background:#222;display:flex;align-items:center;justify-content:center}
.nav{left:474px;top:82px;display:flex;gap:36px;color:var(--white);font-size:14px}
.quote-btn{left:973px;top:72px;width:115px;height:40px;background:var(--red);color:var(--white);font-size:13px;display:flex;align-items:center;justify-content:center;text-transform:uppercase}

/* hero */
.hero{top:127px;height:602px;background:linear-gradient(180deg,#5f6260 0%,#474a48 45%,#2f3a2c 75%,#23281f 100%)}
.hero-arrow{top:240px}
.hero-box{left:113px;top:130px;width:477px;height:327px;background:var(--red);color:var(--white);padding:30px 28px}
.hero-box h1{font-weight:400;font-size:29px;letter-spacing:.5px}
.hero-box p{font-size:12.5px;text-transform:uppercase;line-height:1.7;margin-top:6px;width:410px}
.hero-box ul{list-style:none;margin-top:16px;font-size:13px}
.hero-box li{display:flex;align-items:center;gap:10px;margin-bottom:10px}
.hero-box .ghost{display:inline-block;margin-top:10px;border:1px solid var(--white);padding:10px 16px;font-size:13px;text-transform:uppercase}

.title{font-weight:400;font-size:28px;text-align:center;color:#222}
.title::after{content:"";display:block;width:30px;height:2px;background:var(--red);margin:12px auto 0}

/* about */
.about{top:729px;height:327px}
.about .title{margin-top:36px}
.about-intro{width:1010px;margin:30px auto 0;text-align:center;font-size:12px;line-height:1.7}
.features{left:113px;top:190px;display:flex;gap:0}
.feature{width:357px;display:flex;gap:14px}
.feature h3{color:var(--red);font-size:16px;font-weight:600;text-transform:uppercase}
.feature p{font-size:12px;line-height:1.65;margin-top:6px;width:210px;color:#666}

/* gallery */
.gallery{top:1056px;height:745px;background:linear-gradient(120deg,var(--maroon-a) 0%,#6b1428 50%,var(--maroon-b) 100%)}
.gallery .title{color:var(--white);margin-top:44px}
.filters{left:333px;top:136px;display:flex;gap:18px}
.filters span{height:40px;padding:0 24px;border:1px solid var(--white);color:var(--white);font-size:13px;display:flex;align-items:center;text-transform:uppercase}
.filters .on{background:var(--white);color:var(--red)}
.card{width:229px;height:179px;border:5px solid var(--white);background:linear-gradient(160deg,#4b3a33,#2a211d);color:var(--white);text-align:center;padding:34px 16px 0}
.card h4{font-weight:400;font-size:17px;text-transform:uppercase}
.card p{font-size:11px;line-height:1.6;margin-top:10px}
.card.photo{background:linear-gradient(150deg,#cfc7b3,#8a5a3a 60%,#6a3c22)}
.tagline{left:323px;top:673px;color:var(--white);font-size:16px;font-weight:600}
.tag-btn{left:760px;top:653px;width:115px;height:38px;border:1px solid var(--white);color:var(--white);font-size:13px;display:flex;align-items:center;justify-content:center;text-transform:uppercase}

/* current project */
.current{top:1801px;height:465px;background:repeating-linear-gradient(45deg,#f4f4f4 0 14px,#ececec 14px 15px)}
.aerial{left:0;top:0;width:532px;height:465px;background:linear-gradient(160deg,#3d4540,#242a27 60%,#1a1e1c)}
.current .heading{left:0;width:1200px;top:52px;text-align:center;font-size:28px;color:#222}
.current .heading span{color:var(--white)}
.project-photo{left:376px;top:142px;width:370px;height:257px;border:5px solid var(--white);background:linear-gradient(150deg,#d9d3c2,#9c6a44 60%,#6f4126);box-shadow:0 2px 8px rgba(0,0,0,.25)}
.project-info{left:766px;top:112px;width:326px;text-align:center}
.project-info .mini{width:60px;height:56px;border:1px solid #bbb;margin:0 auto;display:flex;align-items:center;justify-content:center;font-size:9px;font-weight:700;color:var(--red)}
.project-info h3{color:var(--red);font-weight:400;font-size:17px;line-height:1.6;margin-top:24px}
.project-info p{font-size:12px;line-height:1.75;margin-top:12px}
.project-info .btn{display:inline-block;margin-top:14px;border:1px solid var(--red);color:var(--red);font-size:11px;padding:5px 10px;text-transform:uppercase}

/* testimonials */
.testimonials{top:2266px;height:495px;background:linear-gradient(180deg,#fff 40%,#eeeeee 100%)}
.testimonials .title{margin-top:60px}
.t-card{top:208px;width:300px;height:217px;background:var(--white);border:1px solid #ddd;text-align:center;padding:0 28px}
.t-card p{font-style:italic;font-size:12px;line-height:1.75;margin-top:62px;color:#666}
.t-card .name{margin-top:28px;border-top:1px solid #ddd;padding-top:14px;font-size:11px;text-transform:uppercase;color:#666}
.hex{top:150px}

/* footer */
.footer{top:2761px;height:298px;background:var(--footer);color:var(--white)}
.footer h5{font-weight:400;font-size:16px;text-transform:uppercase}
.footer p,.footer li{font-size:12px;line-height:1.7;color:#ccc}
.news{left:113px;top:78px;width:300px}
.subscribe{left:113px;top:164px;display:flex}
.subscribe span{width:201px;height:40px;background:var(--white);color:#888;font-size:12px;display:flex;align-items:center;padding-left:10px}
.subscribe b{width:96px;height:40px;background:var(--red);font-size:12px;display:flex;align-items:center;justify-content:center;font-weight:600;text-transform:uppercase}
.menu{left:497px;top:78px}
.menu ul{list-style:none;margin-top:12px}
.menu li{margin-bottom:5px}
.menu li::before{content:"» ";color:var(--white)}
.contact{left:729px;top:78px;width:360px}
.c-row{display:flex;gap:16px;align-items:center;margin-top:14px}
.c-row .ic{width:36px;height:36px;border:1px solid #555;display:flex;align-items:center;justify-content:center;flex:none}
.c-row strong{font-size:14px;font-weight:400}
.c-row em{color:#3b8fd8;font-style:normal;font-size:11px;display:block}
.to-top{left:578px;top:4px;width:44px;height:44px;border-radius:50%;background:var(--red)}
.bottom{top:3059px;height:127px;background:#1c1c1c;border-top:1px solid #333;text-align:center}
.bottom .social{left:518px;top:28px}
.bottom p{position:absolute;left:0;width:1200px;top:80px;font-size:11px;color:#bbb}
</style>
</head>
<body>

<header class="section header">
  <svg class="abs logo-area" viewBox="0 0 310 127" aria-hidden="true"><polygon points="0,0 250,0 306,63 250,127 0,127" fill="#fff"/></svg>
  <div class="abs brand"><span class="brand-mark"></span><span class="brand-name">Dovin Pratchell Homes</span></div>
  <div class="abs social"><span></span><span></span><span></span><span></span></div>
  <div class="abs contact-item" style="left:786px">
    <span class="ic"><svg width="16" height="12" viewBox="0 0 16 12"><rect x="0.5" y="0.5" width="15" height="11" fill="none" stroke="#999"/><path d="M1 1l7 6 7-6" fill="none" stroke="#999"/></svg></span>
    <div>Email<small>info@domain.com</small></div>
  </div>
  <div class="abs contact-item" style="left:952px">
    <span class="ic"><svg width="16" height="16" viewBox="0 0 16 16"><path d="M3 1l3 3-2 2c1 2 3 4 5 5l2-2 3 3-2 3C7 14 2 9 1 3z" fill="#999"/></svg></span>
    <div>Call Now<small>info@domain.com</small></div>
  </div>
  <nav class="abs nav"><span>Home</span><span>About Us</span><span>Gallery</span><span>Testimonials</span><span>Contact Info</span></nav>
  <div class="abs quote-btn">Get a Quote</div>
</header>

<section class="section hero" role="img" aria-label="Photo of a finished two-storey stone and siding family home with lawn">
  <svg class="abs hero-arrow" style="left:20px" width="24" height="70" viewBox="0 0 24 70"><path d="M22 2L3 35l19 33" fill="none" stroke="#ddd" stroke-width="2"/></svg>
  <svg class="abs hero-arrow" style="left:1156px" width="24" height="70" viewBox="0 0 24 70"><path d="M2 2l19 33L2 68" fill="none" stroke="#ddd" stroke-width="2"/></svg>
  <div class="abs hero-box">
    <h1>WELCOME TO DOVIN PRATCHELL</h1>
    <p>It is a long established fact that a reader will be distract by the readable content of a page when looking at its layout.</p>
    <ul>
      <li><svg width="14" height="14" viewBox="0 0 14 14"><rect x=".5" y=".5" width="13" height="13" fill="none" stroke="#fff"/><path d="M3 7l3 3 5-6" fill="none" stroke="#fff" stroke-width="1.5"/></svg>Building of your Dream</li>
      <li><svg width="14" height="14" viewBox="0 0 14 14"><rect x=".5" y=".5" width="13" height="13" fill="none" stroke="#fff"/><path d="M3 7l3 3 5-6" fill="none" stroke="#fff" stroke-width="1.5"/></svg>We 'll Take Care Your Opinion and Hope</li>
      <li><svg width="14" height="14" viewBox="0 0 14 14"><rect x=".5" y=".5" width="13" height="13" fill="none" stroke="#fff"/><path d="M3 7l3 3 5-6" fill="none" stroke="#fff" stroke-width="1.5"/></svg>Best Architecture We have</li>
    </ul>
    <span class="ghost">Get a Quote</span>
  </div>
</section>

<section class="section about">
  <h2 class="title">About Us</h2>
  <p class="about-intro">It is a long established fact that a reader will be distracted by the readable content of a page when looking at its layout. The point of using Lorem Ipsum is that it has a more-or-less normal distribution of letters, as opposed to using 'Content here, content here.</p>
  <div class="abs features">
    <div class="feature">
      <svg width="34" height="30" viewBox="0 0 34 30"><rect x="2" y="6" width="30" height="20" rx="3" fill="none" stroke="#b3060d" stroke-width="2"/><rect x="22" y="12" width="10" height="8" fill="none" stroke="#b3060d" stroke-width="2"/></svg>
      <div><h3>Reasonable Price</h3><p>Established fact that a readbe distracted by the readable content of a page when looking at its layout.</p></div>
    </div>
    <div class="feature">
      <svg width="34" height="40" viewBox="0 0 34 40"><circle cx="17" cy="14" r="11" fill="none" stroke="#b3060d" stroke-width="2"/><circle cx="17" cy="14" r="5" fill="none" stroke="#b3060d" stroke-width="2"/><path d="M10 23l-3 14 10-5 10 5-3-14" fill="none" stroke="#b3060d" stroke-width="2"/></svg>
      <div><h3>Certified Engineer</h3><p>Established fact that a readbe distracted by the readable content of a page when looking at its layout.</p></div>
    </div>
    <div class="feature">
      <svg width="34" height="38" viewBox="0 0 34 38"><path d="M4 2h20l6 6v28H4z" fill="none" stroke="#b3060d" stroke-width="2"/><path d="M9 14h16M9 20h16M9 26h10" stroke="#b3060d" stroke-width="2"/></svg>
      <div><h3>Guranteed Works</h3><p>Established fact that a readbe distracted by the readable content of a page when looking at its layout.</p></div>
    </div>
  </div>
</section>

<section class="section gallery">
  <h2 class="title">Project Gallery</h2>
  <div class="abs filters"><span class="on">Show All</span><span>Building</span><span>Interior</span><span>Architecture</span></div>
  <div class="abs card photo" style="left:113px;top:218px" role="img" aria-label="Photo of a wooden staircase in a new home interior"></div>
  <div class="abs card" style="left:361px;top:218px"><h4>Interior</h4><p>Established fact that a readbe distracted by the readable content of a page when.</p></div>
  <div class="abs card" style="left:610px;top:218px"><h4>Architech</h4><p>Established fact that a readbe distracted by the readable content of a page when.</p></div>
  <div class="abs card" style="left:858px;top:218px"><h4>Interior</h4><p>Established fact that a readbe distracted by the readable content of a page when.</p></div>
  <div class="abs card" style="left:113px;top:416px"><h4>Building</h4><p>Established fact that a readbe distracted by the readable content of a page when.</p></div>
  <div class="abs card" style="left:361px;top:416px"><h4>Interior</h4><p>Established fact that a readbe distracted by the readable content of a page when.</p></div>
  <div class="abs card" style="left:610px;top:416px"><h4>Architech</h4><p>Established fact that a readbe distracted by the readable content of a page when.</p></div>
  <div class="abs card" style="left:858px;top:416px"><h4>Interior</h4><p>Established fact that a readbe distracted by the readable content of a page when.</p></div>
  <div class="abs tagline">WE BUILD PROFESSIONAL AND SMART BUILDINGS</div>
  <div class="abs tag-btn">Get a Quote</div>
</section>

<section class="section current">
  <div class="abs aerial" role="img" aria-label="Aerial photo of a residential neighbourhood at dusk"></div>
  <div class="abs heading"><span>Current </span>Project</div>
  <div class="abs project-photo" role="img" aria-label="Photo of a wooden staircase and hallway in the current project"></div>
  <div class="abs project-info">
    <div class="mini">DOVIN PRATCHELL</div>
    <h3>Consectetuer Adipiscing Elit,<br>Sed Diam Nonummy</h3>
    <p>Lorem ipsum dolor sit amet,<br>mi euismod tincidunt ut laoreet dolore magna aliquam erat volutpat. Ut wisi enim ad minim veniam, quisnostrud ex tation ullamcorper suscipit lobortis nisl ut aliquip ex ea commodo consequat.</p>
    <span class="btn">View Details</span>
  </div>
</section>

<section class="section testimonials">
  <h2 class="title">Testimonials</h2>
  <div class="abs t-card" style="left:113px"><p>Contrary to popular belief, Lorem Ipsum is not simply random text. It has roots in a piece of classical Latin literature from 45 BC, making it over 2000 years old. Tobias</p><div class="name">Customer Name</div></div>
  <div class="abs t-card" style="left:450px"><p>Contrary to popular belief, Lorem Ipsum is not simply random text. It has roots in a piece of classical Latin literature from 45 BC, making it over 2000 years old. Tobias</p><div class="name">Customer Name</div></div>
  <div class="abs t-card" style="left:786px"><p>Contrary to popular belief, Lorem Ipsum is not simply random text. It has roots in a piece of classical Latin literature from 45 BC, making it over 2000 years old. Tobias</p><div class="name">Customer Name</div></div>
  <svg class="abs hex" style="left:214px" width="96" height="110" viewBox="0 0 96 110"><polygon points="48,2 94,28 94,82 48,108 2,82 2,28" fill="#e4e4e4"/></svg>
  <svg class="abs hex" style="left:552px" width="96" height="110" viewBox="0 0 96 110"><polygon points="48,2 94,28 94,82 48,108 2,82 2,28" fill="#e4e4e4"/></svg>
  <svg class="abs hex" style="left:888px" width="96" height="110" viewBox="0 0 96 110"><polygon points="48,2 94,28 94,82 48,108 2,82 2,28" fill="#e4e4e4"/></svg>
</section>

<footer class="section footer">
  <svg class="abs" style="left:0;top:0" width="1200" height="40" viewBox="0 0 1200 40"><polygon points="0,0 1200,0 1200,2 690,2 640,30 560,30 510,2 0,2" fill="#eeeeee"/></svg>
  <div class="abs to-top"><svg width="44" height="44" viewBox="0 0 44 44"><path d="M16 25l6-6 6 6" fill="none" stroke="#fff" stroke-width="2.5"/></svg></div>
  <div class="abs news"><h5>Newsletter Signup</h5><p style="margin-top:10px">Contrary to popular belief, Lorem Ipsum is not simply random text.</p></div>
  <div class="abs subscribe"><span>Enter your Email Id</span><b>Subscribe</b></div>
  <div class="abs menu"><h5>Quick Menu</h5><ul><li>Home</li><li>About Us</li><li>Gallery</li><li>Testimonials</li><li>Contact</li></ul></div>
  <div class="abs contact"><h5>Contact Us</h5>
    <div class="c-row"><span class="ic"><svg width="14" height="14" viewBox="0 0 16 16"><path d="M3 1l3 3-2 2c1 2 3 4 5 5l2-2 3 3-2 3C7 14 2 9 1 3z" fill="#999"/></svg></span><div><strong>0123 456 789, &nbsp; 0123 456 789</strong><em>Please Contact Us</em></div></div>
    <div class="c-row"><span class="ic"><svg width="16" height="12" viewBox="0 0 16 12"><rect x=".5" y=".5" width="15" height="11" fill="none" stroke="#999"/><path d="M1 1l7 6 7-6" fill="none" stroke="#999"/></svg></span><p>yourname@domain.com<br>your2ndname@domain.com</p></div>
    <div class="c-row"><span class="ic"><svg width="12" height="16" viewBox="0 0 12 16"><path d="M6 15S1 9 1 6a5 5 0 0110 0c0 3-5 9-5 9z" fill="#999"/><circle cx="6" cy="6" r="2" fill="#262626"/></svg></span><p>Built by the award , home builder, No.: 215<br>Street main Highway, 478521</p></div>
  </div>
</footer>

<div class="section bottom">
  <div class="abs social"><span></span><span></span><span></span><span></span></div>
  <p>Copy Right © All Rights Reserved . 2017</p>
</div>

</body>
</html>
```